Conference banner for Kestrel training organisation

We empower everyday heroes.
We provide training that empowers individuals to create positive change in themselves, their community, and the world.
We need a large banner design to promote the organisation at conferences and events. We are open to ideas and creativity.
It may involve creatively displaying our logo only, or it may involve our logo and a summary of our products (Kestrel training, Calm Minds Field Care).
Size: 820mm width x 1790mm height
300dpi
Target Market(s)
Educators and frontline health, community, and social workers.
Industry/Entity Type
Training
Colors
Designer to choose colors to be used in the design.

```html
<!DOCTYPE html>
<html lang="en">
<head>
<meta charset="utf-8">
<title>Haven City – Conference Banner</title>
<link rel="stylesheet" href="https://fonts.googleapis.com/css2?family=Montserrat:wght@700&family=Questrial&display=swap">
<style>
  :root {
    --paper: #ffffff;
    --cream: #fcedc6;
    --sand: #f9d592;
    --amber: #f6ad5a;
    --rust: #c9713a;
    --title-blue: #3f8fd8;
    --title-deep: #2a64ad;
    --title-edge: #1a1a1a;
    --band-navy: #0d4a86;
    --band-sky: #a6d2f6;
    --band-text: #f8e4ad;
    --name-blue: #1f57a8;
    --globe-teal: #8fa9a0;
  }
  html, body {
    margin: 0;
    padding: 0;
    width: 1200px;
    height: 1000px;
    overflow: hidden;
    background: var(--paper);
  }
  .canvas {
    position: relative;
    width: 1200px;
    height: 1000px;
  }
  .banner {
    position: absolute;
    left: 0;
    top: 0;
    display: block;
  }
  .title-text {
    font-family: "Montserrat", sans-serif;
    font-weight: 700;
    letter-spacing: 4px;
  }
  .tagline-text {
    font-family: "Questrial", sans-serif;
    fill: var(--band-text);
  }
  .org-name {
    font-family: "Questrial", sans-serif;
    fill: var(--name-blue);
  }
</style>
</head>
<body>
<div class="canvas">
  <svg class="banner" width="1200" height="1000" viewBox="0 0 1200 1000" xmlns="http://www.w3.org/2000/svg">
    <defs>
      <linearGradient id="sky-to-amber" x1="0" y1="0" x2="0" y2="1">
        <stop offset="0" stop-color="var(--cream)"/>
        <stop offset="0.45" stop-color="var(--sand)"/>
        <stop offset="1" stop-color="var(--amber)"/>
      </linearGradient>
      <radialGradient id="globe-shade" cx="0.55" cy="0.35" r="0.75">
        <stop offset="0" stop-color="#e8dcb8"/>
        <stop offset="0.6" stop-color="var(--globe-teal)"/>
        <stop offset="1" stop-color="var(--rust)"/>
      </radialGradient>
      <linearGradient id="title-fill" x1="0" y1="0" x2="0" y2="1">
        <stop offset="0" stop-color="var(--title-blue)"/>
        <stop offset="1" stop-color="var(--title-deep)"/>
      </linearGradient>
    </defs>

    <!-- banner field -->
    <rect class="banner-field" x="0" y="208" width="1200" height="548" fill="url(#sky-to-amber)"/>
    <path class="sweep" d="M0 230 C 400 200, 800 230, 1200 300 L1200 208 L0 208 Z" fill="#fff6dd" opacity="0.6"/>

    <!-- globe illustration area -->
    <g role="img" aria-label="Stylised globe with orbit lines">
      <clipPath id="field-clip"><rect x="0" y="208" width="1200" height="548"/></clipPath>
      <circle cx="-40" cy="560" r="320" fill="url(#globe-shade)" opacity="0.75" clip-path="url(#field-clip)"/>
    </g>
    <path class="orbit-line" d="M282 290 C 300 420, 290 620, 230 756" fill="none" stroke="#fff3d6" stroke-width="2" opacity="0.8"/>

    <!-- organisation name in place of mark -->
    <g class="org-lockup">
      <circle cx="70" cy="494" r="14" fill="var(--name-blue)"/>
      <text class="org-name" x="94" y="504" font-size="28">Haven City</text>
    </g>

    <!-- headline -->
    <text class="title-text" x="294" y="512" font-size="132" textLength="866" lengthAdjust="spacingAndGlyphs"
          fill="var(--title-edge)" transform="translate(-4 2)">HAVEN CITY</text>
    <text class="title-text" x="294" y="512" font-size="132" textLength="866" lengthAdjust="spacingAndGlyphs"
          fill="url(#title-fill)" stroke="#ffffff" stroke-width="2.5" paint-order="stroke">HAVEN CITY</text>

    <!-- tagline band -->
    <path class="band-sky" d="M360 580 L1200 566 L1200 592 L332 618 Z" fill="var(--band-sky)"/>
    <path class="band-navy" d="M284 520 L1200 520 L1200 566 L364 574 L312 594 Z" fill="var(--band-navy)"/>
    <text class="tagline-text" x="316" y="563" font-size="37" textLength="856" lengthAdjust="spacingAndGlyphs">KESTREL TRAINING, CALM MINDS FIELD CARE</text>
  </svg>
</div>
</body>
</html>
```